A 3d printing services company "The Velvet Lattice" needs a clutter breaking business card design

The Velvet Lattice is a 3d design, animation and printing services company. We are in the B2B and B2C space. www.velvetlattice.com.sg
We have been in business for a year.
The logo is already done (the current file is attached).
We need a business card design which reflects the 3d printing and animations services of the company. A standard rectangular shape is not an option. The card can be die cut.
The card should have the colors of the logo and should have a high tech wow feel to it.
The front of the card should have my name, designation, cellphone email and website details. No need for an office address.
Name: Raghavan Kulkarni
Designation: Founder Director
Cellphone (65)91827345
email: raghavan@velvetlattice.com.sg
website: www.velvetlattice.com.sg
The back of the card should have the services we offer:
1. 3d Design and Modelling
2. 3d Animation
3. 3D Printing
The tag line is: "make your ideas real"
Am uploading the current business card files(back and front).
Target Market(s)
Business owners and C level managers in Marine, Healthcare industry
Industry/Entity Type
Printing
Contact Information for Business Card
Name: Raghavan Kulkarni
Cellphone (65)91827345
2. 3d Animation
3. 3D Printing

```html
<!DOCTYPE html>
<html lang="en">
<head>
<meta charset="utf-8">
<title>The Velvet Lattice – Business Card</title>
<link rel="stylesheet" href="https://fonts.googleapis.com/css2?family=Arimo:wght@400;700&family=Exo+2:wght@600&family=Tinos&display=swap">
<style>
  :root {
    --backdrop: #1c1c1c;
    --navy-deep: #04132a;
    --navy: #0b2c5c;
    --blue: #1f63c4;
    --blue-bright: #2c7be0;
    --blue-soft: #1d4f9e;
    --green: #3aa53a;
    --green-pale: #a6c796;
    --paper-light: #f3f3f3;
    --paper-mid: #cfcfcf;
    --ink: #3a3a3a;
  }
  * { margin: 0; padding: 0; box-sizing: border-box; }
  html, body { width: 1200px; height: 1000px; overflow: hidden; }
  body { background: var(--backdrop); position: relative; font-family: "Arimo", Arial, sans-serif; }

  .card { position: absolute; top: 276px; width: 574px; height: 335px; overflow: hidden; }

  /* Back side: services */
  .card--back {
    left: 22px;
    background:
      linear-gradient(115deg, transparent 45%, rgba(60,120,210,0.10) 60%, transparent 75%),
      radial-gradient(ellipse at 72% 45%, var(--navy) 0%, var(--navy-deep) 80%);
  }
  .back__visual {
    position: absolute; left: 0; top: 0; width: 290px; height: 335px;
    background:
      radial-gradient(ellipse 60% 55% at 18% 45%, rgba(58,165,58,0.55) 0%, rgba(58,165,58,0) 70%),
      radial-gradient(ellipse 95% 95% at 20% 50%, rgba(40,95,190,0.85) 0%, rgba(20,60,130,0.55) 55%, rgba(4,19,42,0) 100%);
  }
  .brand-mark {
    position: absolute; left: 290px; top: 44px; width: 44px; height: 44px;
    border-radius: 50%; background: var(--blue-soft);
  }
  .services { position: absolute; left: 365px; top: 33px; list-style: none; color: var(--blue); font-size: 17px; line-height: 20px; letter-spacing: 0.3px; }
  .brand-name {
    position: absolute; left: 290px; top: 112px; width: 270px;
    font-family: "Exo 2", Arial, sans-serif; font-weight: 600;
    color: var(--green); font-size: 54px; line-height: 64px; letter-spacing: -0.5px;
  }
  .tagline { position: absolute; left: 292px; top: 291px; color: var(--blue); font-size: 21px; letter-spacing: 0.3px; }

  /* Front side: contact */
  .card--front {
    left: 605px;
    background: linear-gradient(135deg, var(--paper-light) 0%, #e2e2e2 50%, var(--paper-mid) 100%);
  }
  .front__visual {
    position: absolute; left: 250px; top: 0; width: 324px; height: 335px;
    clip-path: polygon(38% 0, 100% 0, 100% 100%, 0 100%, 10% 55%);
    background: linear-gradient(160deg, rgba(166,199,150,0.75) 0%, rgba(150,190,130,0.9) 100%);
  }
  .person { position: absolute; left: 42px; top: 46px; }
  .person__name { font-size: 24px; font-weight: 700; color: var(--ink); letter-spacing: -0.2px; }
  .person__name .first { color: var(--green); }
  .person__role { font-size: 15px; letter-spacing: 3.6px; color: var(--ink); margin-top: 1px; }
  .contact { position: absolute; left: 42px; top: 183px; border-left: 2px solid var(--green); padding-left: 22px; height: 87px; }
  .contact__row { display: flex; align-items: center; gap: 14px; font-size: 15px; letter-spacing: 0.8px; color: var(--ink); height: 25px; }
  .contact__row--phone { font-family: "Tinos", "Times New Roman", serif; font-size: 17px; letter-spacing: 0.3px; }
  .contact__row svg { width: 12px; height: 12px; flex: none; }
  .contact__label { font-size: 15px; font-weight: 700; color: var(--green); margin-top: 7px; }
  .contact__web { font-size: 15px; letter-spacing: 1.2px; color: var(--ink); }
</style>
</head>
<body>

<section class="card card--back">
  <div class="back__visual" role="img" aria-label="Glossy blue and green dimensional brand graphic"></div>
  <span class="brand-mark"></span>
  <ul class="services">
    <li>Design and Modelling</li>
    <li>Animation</li>
    <li>Printing</li>
  </ul>
  <h1 class="brand-name">The Velvet Lattice</h1>
  <p class="tagline">make your ideas real</p>
</section>

<section class="card card--front">
  <div class="front__visual" role="img" aria-label="Large faint green dimensional brand graphic"></div>
  <div class="person">
    <h2 class="person__name"><span class="first">Raghavan</span>Kulkarni</h2>
    <p class="person__role">Founder Director</p>
  </div>
  <div class="contact">
    <p class="contact__row contact__row--phone">
      <svg viewBox="0 0 24 24"><path fill="var(--green)" d="M6.6 10.8a15.1 15.1 0 0 0 6.6 6.6l2.2-2.2a1 1 0 0 1 1-.25 11.4 11.4 0 0 0 3.6.57 1 1 0 0 1 1 1V20a1 1 0 0 1-1 1A17 17 0 0 1 3 4a1 1 0 0 1 1-1h3.5a1 1 0 0 1 1 1c0 1.25.2 2.45.57 3.57a1 1 0 0 1-.25 1z"/></svg>
      (65)91827345
    </p>
    <p class="contact__row">
      <svg viewBox="0 0 24 24"><rect x="2" y="5" width="20" height="14" fill="var(--green)"/><path d="M2 5l10 8 10-8" fill="none" stroke="#fff" stroke-width="2"/></svg>
      raghavan@velvetlattice.com.sg
    </p>
    <p class="contact__label">Website</p>
    <p class="contact__web">www.velvetlattice.com.sg</p>
  </div>
</section>

</body>
</html>
```